I need a DVD cover for a training package contained on a disc. There are four modules within the resource so I need these to be visible on the cover. They are:
Cultural Competence Healthcare Provision
Provision of Care to CALD Women having Babies in Australia
Cultural Considerations in Aged Care Provision
Cultural Competence in Mental Health

I have attached a cd cover with an image of a waratah. This is Bellmore Ridge Valley Health's logo so needs to appear on the front cover also.
The smaller logo with the waratah also needs to be on the front cover. Please note these are the only copies I could obtain so if the quality is too poor you may need to reproduce.

The following should appear on the back cover:
‘Pathways to Inclusive Patient Support’ is a collaborative achievement of the Multicultural Health Liaison Officers in Acute Care, Obstetrics, Aged Care and Mental Health under the guidance of the Director, Multicultural Health Service in Bellmore Ridge Valley Local Health District. Staff members from the specialist teams and community members graciously contributed to the production of podcasts and video clips.
Photography, video clips and technical support was provided by Daniel Follett - E-learning Developer and Designer - Lumen Tutors.
This project was coordinated by Colleen Bastow, Multicultural Health Liaison Officer (Acute Care, Lower Brindlewood Coastal Hospital Network).

```html
<!DOCTYPE html>
<html lang="en">
<head>
<meta charset="utf-8">
<title>DVD Cover and Disc Label – Pathways to Inclusive Patient Support</title>
<link rel="stylesheet" href="https://fonts.googleapis.com/css2?family=Montserrat:wght@300;400;600;700&family=Arimo:wght@400;700&display=swap">
<style>
  :root {
    --page: #ffffff;
    --ink: #1d1d1b;
    --navy: #2b3a7d;
    --sky: #8fc6e8;
    --sky-soft: #d9ecf8;
    --red: #c8203d;
    --red-soft: rgba(200, 32, 61, 0.55);
  }
  * { box-sizing: border-box; margin: 0; padding: 0; }
  html, body { width: 1200px; height: 900px; overflow: hidden; background: var(--page); }
  body { position: relative; font-family: "Montserrat", Arial, sans-serif; color: var(--ink); }

  /* ---------- sheet captions ---------- */
  .caption {
    position: absolute; font-family: "Arimo", Arial, sans-serif; font-size: 13px; color: var(--ink);
    text-align: center; width: 560px;
  }
  .caption strong { font-weight: 700; }

  /* ---------- DVD coversheet ---------- */
  .coversheet {
    position: absolute; top: 55px; width: 558px; height: 373px; overflow: hidden;
    background: linear-gradient(200deg, var(--sky) 0%, var(--sky-soft) 18%, #ffffff 48%);
    box-shadow: 0 2px 5px rgba(0,0,0,0.28);
  }
  .coversheet--blue { left: 30px; }
  .coversheet--red { left: 615px; }

  .back-cover { position: absolute; left: 0; top: 0; width: 268px; height: 100%; background: #ffffff; }
  .office { position: absolute; top: 28px; width: 112px; font-size: 5.2px; line-height: 1.25; color: var(--navy); }
  .office--head { left: 18px; }
  .office--regional { left: 137px; }
  .office h3 { font-size: 5.4px; font-weight: 700; color: var(--red); margin-bottom: 8px; }
  .office h4 { font-size: 5.2px; font-weight: 700; margin-top: 5px; }
  .office h3 + h4 { margin-top: 0; }
  .disclaimer { position: absolute; left: 18px; top: 192px; width: 112px; font-size: 4.9px; line-height: 1.32; color: var(--navy); }
  .disclaimer h4 { font-size: 5.2px; font-weight: 700; margin-bottom: 4px; }
  .web-address { position: absolute; left: 18px; top: 346px; font-size: 7px; color: var(--red); }

  .spine { position: absolute; left: 268px; top: 0; width: 24px; height: 100%; }
  .spine-titles {
    position: absolute; left: 22px; top: 14px; width: 270px; transform-origin: 0 0; transform: rotate(90deg);
    font-size: 5.6px; line-height: 1.5; color: var(--navy); font-weight: 300;
  }
  .coversheet--red .spine-titles { color: var(--red); }
  .spine-brand {
    position: absolute; left: 20px; top: 292px; width: 70px; transform-origin: 0 0; transform: rotate(90deg);
    display: flex; align-items: center; gap: 3px; font-size: 5.4px; font-weight: 600; color: var(--navy);
  }
  .brand-mark { width: 6px; height: 6px; background: var(--red); flex: none; }

  .emblem-area {
    position: absolute; left: 130px; top: 196px; width: 340px; height: 162px;
    background: radial-gradient(ellipse at 50% 70%, var(--red-soft) 0%, rgba(200,32,61,0.25) 45%, rgba(200,32,61,0) 72%);
  }

  .front-brand {
    position: absolute; right: 22px; top: 20px; display: flex; align-items: center; gap: 6px;
    font-size: 10.5px; font-weight: 600; color: var(--navy); width: 150px; line-height: 1.15;
  }
  .front-brand .brand-mark { width: 14px; height: 14px; }

  .modules { position: absolute; right: 22px; top: 96px; width: 230px; list-style: none; text-align: right; }
  .modules li { font-size: 10.6px; font-weight: 300; line-height: 1.22; margin-bottom: 9px; color: var(--navy); }
  .coversheet--red .modules li { color: var(--red); }

  /* ---------- disc label ---------- */
  .disc {
    position: absolute; left: 432px; top: 462px; width: 336px; height: 336px; border-radius: 50%; overflow: hidden;
    background: linear-gradient(135deg, #ffffff 35%, var(--sky-soft) 70%, var(--sky) 100%);
    border: 1px dashed #555;
  }
  .disc-hole {
    position: absolute; left: 110px; top: 110px; width: 114px; height: 114px; border-radius: 50%;
    background: var(--page); border: 1px dashed #555;
  }
  .disc-emblem-area {
    position: absolute; left: 0; top: 40px; width: 180px; height: 290px;
    background: radial-gradient(ellipse at 30% 60%, var(--red-soft) 0%, rgba(200,32,61,0.25) 45%, rgba(200,32,61,0) 72%);
  }
  .disc-title { position: absolute; left: 0; width: 100%; top: 48px; text-align: center; font-size: 12.5px; font-weight: 700; color: var(--red); line-height: 1.25; }
  .disc-producer { position: absolute; left: 0; width: 100%; top: 84px; text-align: center; font-size: 7px; color: var(--navy); line-height: 1.3; }
  .disc-producer strong { font-weight: 700; }
  .disc-brand {
    position: absolute; left: 190px; top: 248px; display: flex; align-items: center; gap: 5px;
    font-size: 8.5px; font-weight: 600; color: var(--navy); width: 130px; line-height: 1.15;
  }
  .disc-brand .brand-mark { width: 11px; height: 11px; }
</style>
</head>
<body>

  <section class="coversheet coversheet--blue" aria-label="DVD coversheet with blue titles">
    <div class="back-cover">
      <div class="office office--head">
        <h3>Head Office – Harwick</h3>
        <h4>Street address:</h4>
        <p>Summit Road<br>East Carrow NSW 2990<br>Australia</p>
        <h4>Postal address:</h4>
        <p>Locked Bag 4<br>East Carrow NSW 2990<br>Australia</p>
        <h4>Telephone:</h4>
        <p>within Australia 02 5550 1000<br>outside Australia 61 2 5550 1000</p>
        <h4>Fax:</h4>
        <p>within Australia 02 5550 1099<br>outside Australia 61 2 5550 1099</p>
        <h4>Email address:</h4>
        <p>contact@brvhealth.example.au</p>
      </div>
      <div class="office office--regional">
        <h3>Regional Head Office – Corrandale</h3>
        <h4>Street address:</h4>
        <p>Kestrel House<br>Suite 3, 210-214 Arden Street<br>Corrandale NSW 2991<br>Australia</p>
        <h4>Postal address:</h4>
        <p>Locked Mail Bag 5120<br>Corrandale NSW 2991<br>Australia</p>
        <h4>Telephone:</h4>
        <p>within Australia 02 5550 2200<br>outside Australia 61 2 5550 2200</p>
        <h4>Fax:</h4>
        <p>within Australia 02 5550 2299<br>outside Australia 61 2 5550 2299</p>
        <h4>Email address:</h4>
        <p>contact@brvhealth.example.au</p>
      </div>
      <div class="disclaimer">
        <h4>Disclaimer:</h4>
        <p>‘Pathways to Inclusive Patient Support’ is a collaborative achievement of the Multicultural Health Liaison Officers in Acute Care, Obstetrics, Aged Care and Mental Health under the guidance of the Director, Multicultural Health Service in Bellmore Ridge Valley Local Health District. Staff members from the specialist teams and community members graciously contributed to the production of podcasts and video clips. Photography, video clips and technical support was provided by Daniel Follett - E-learning Developer and Designer - Lumen Tutors. This project was coordinated by Colleen Bastow, Multicultural Health Liaison Officer (Acute Care, Lower Brindlewood Coastal Hospital Network).</p>
      </div>
      <p class="web-address">www.brvhealth.example.au</p>
    </div>
    <div class="emblem-area" role="img" aria-label="Large health district flower emblem spanning back, spine and front"></div>
    <div class="spine">
      <p class="spine-titles">Cultural Competence Healthcare Provision • Provision of Care to CALD Women having Babies in Australia • Cultural Considerations in Aged Care Provision • Cultural Competence in Mental Health</p>
      <div class="spine-brand"><span class="brand-mark"></span>Bellmore Ridge Valley Health</div>
    </div>
    <div class="front-brand"><span class="brand-mark"></span>Bellmore Ridge Valley Local Health District</div>
    <ul class="modules">
      <li>Cultural Competence Healthcare Provision</li>
      <li>Provision of Care to CALD Women<br>having Babies in Australia</li>
      <li>Cultural Considerations in Aged<br>Care Provision</li>
      <li>Cultural Competence in Mental Health</li>
    </ul>
  </section>
  <p class="caption" style="left:30px; top:445px;"><strong>Design 2.1:</strong> DVD Coversheet text in blue.</p>

  <section class="coversheet coversheet--red" aria-label="DVD coversheet with red titles">
    <div class="back-cover">
      <div class="office office--head">
        <h3>Head Office – Harwick</h3>
        <h4>Street address:</h4>
        <p>Summit Road<br>East Carrow NSW 2990<br>Australia</p>
        <h4>Postal address:</h4>
        <p>Locked Bag 4<br>East Carrow NSW 2990<br>Australia</p>
        <h4>Telephone:</h4>
        <p>within Australia 02 5550 1000<br>outside Australia 61 2 5550 1000</p>
        <h4>Fax:</h4>
        <p>within Australia 02 5550 1099<br>outside Australia 61 2 5550 1099</p>
        <h4>Email address:</h4>
        <p>contact@brvhealth.example.au</p>
      </div>
      <div class="office office--regional">
        <h3>Regional Head Office – Corrandale</h3>
        <h4>Street address:</h4>
        <p>Kestrel House<br>Suite 3, 210-214 Arden Street<br>Corrandale NSW 2991<br>Australia</p>
        <h4>Postal address:</h4>
        <p>Locked Mail Bag 5120<br>Corrandale NSW 2991<br>Australia</p>
        <h4>Telephone:</h4>
        <p>within Australia 02 5550 2200<br>outside Australia 61 2 5550 2200</p>
        <h4>Fax:</h4>
        <p>within Australia 02 5550 2299<br>outside Australia 61 2 5550 2299</p>
        <h4>Email address:</h4>
        <p>contact@brvhealth.example.au</p>
      </div>
      <div class="disclaimer">
        <h4>Disclaimer:</h4>
        <p>‘Pathways to Inclusive Patient Support’ is a collaborative achievement of the Multicultural Health Liaison Officers in Acute Care, Obstetrics, Aged Care and Mental Health under the guidance of the Director, Multicultural Health Service in Bellmore Ridge Valley Local Health District. Staff members from the specialist teams and community members graciously contributed to the production of podcasts and video clips. Photography, video clips and technical support was provided by Daniel Follett - E-learning Developer and Designer - Lumen Tutors. This project was coordinated by Colleen Bastow, Multicultural Health Liaison Officer (Acute Care, Lower Brindlewood Coastal Hospital Network).</p>
      </div>
      <p class="web-address">www.brvhealth.example.au</p>
    </div>
    <div class="emblem-area" role="img" aria-label="Large health district flower emblem spanning back, spine and front"></div>
    <div class="spine">
      <p class="spine-titles">Cultural Competence Healthcare Provision • Provision of Care to CALD Women having Babies in Australia • Cultural Considerations in Aged Care Provision • Cultural Competence in Mental Health</p>
      <div class="spine-brand"><span class="brand-mark"></span>Bellmore Ridge Valley Health</div>
    </div>
    <div class="front-brand"><span class="brand-mark"></span>Bellmore Ridge Valley Local Health District</div>
    <ul class="modules">
      <li>Cultural Competence Healthcare Provision</li>
      <li>Provision of Care to CALD Women<br>having Babies in Australia</li>
      <li>Cultural Considerations in Aged<br>Care Provision</li>
      <li>Cultural Competence in Mental Health</li>
    </ul>
  </section>
  <p class="caption" style="left:612px; top:445px;"><strong>Design 2.2:</strong> DVD Coversheet text in red.</p>

  <section class="disc" aria-label="Disc label">
    <div class="disc-emblem-area" role="img" aria-label="Health district flower emblem wrapping the left of the disc"></div>
    <div class="disc-hole"></div>
    <h2 class="disc-title">Pathways to<br>Inclusive Patient Support</h2>
    <p class="disc-producer">Produced by<br><strong>Multicultural Health Service<br>P.O. Box 406 Farrowdale NSW 2992</strong></p>
    <div class="disc-brand"><span class="brand-mark"></span>Bellmore Ridge Valley Local Health District</div>
  </section>
  <p class="caption" style="left:320px; top:820px;"><strong>Design 2:</strong> CD Label</p>

</body>
</html>
```